Letterhead for Clean city delivery Logistics needed

Dear all,

we are looking for a powerful design for our letterhead. We are a Berlin-based (Germany) logistics company which delivers parcel on the last mile in a sustainable way. Design should communicate: sustainability, integrity, one family, performance-focused, passionate for excellence and customer experience. Please find company logo attached.

Looking forward for

```html
<!DOCTYPE html>
<html lang="en">
<head>
<meta charset="utf-8">
<title>Halden Parcel Letterhead</title>
<link href="https://fonts.googleapis.com/css2?family=Open+Sans:wght@400;700&display=swap" rel="stylesheet">
<style>
  :root {
    --backdrop: #ebebeb;
    --paper: #ffffff;
    --green: #1a9a48;
    --ink: #4a4a4a;
    --ink-dark: #2f2f2f;
    --ink-soft: #7a7a7a;
    --signature-tone: #d9dde3;
  }
  * { margin: 0; padding: 0; box-sizing: border-box; }
  html, body {
    width: 1200px; height: 874px; overflow: hidden;
    background: var(--backdrop);
    font-family: "Open Sans", Arial, sans-serif;
  }
  .letterhead {
    position: absolute; left: 310px; top: 27px;
    width: 580px; height: 820px;
    background: var(--paper);
    box-shadow: 0 2px 10px rgba(0,0,0,0.08);
    color: var(--ink);
  }
  .brand {
    position: absolute; left: 150px; top: 70px;
    display: flex; flex-direction: column; align-items: flex-start;
  }
  .brand-row { display: flex; align-items: center; gap: 10px; }
  .brand-dot { width: 22px; height: 22px; border-radius: 50%; background: var(--green); }
  .brand-name {
    font-weight: 700; font-size: 26px; letter-spacing: 1px;
    color: var(--green); text-transform: uppercase;
  }
  .brand-tagline {
    margin-left: 32px; margin-top: 2px;
    font-size: 11px; letter-spacing: 1px; color: var(--ink-soft);
  }
  .recipient { position: absolute; left: 70px; top: 230px; line-height: 1.45; font-style: normal; }
  .recipient-name { font-size: 11px; color: var(--ink-dark); text-transform: uppercase; }
  .recipient-detail { font-size: 8.5px; }
  .letter-body {
    position: absolute; left: 110px; top: 295px; width: 350px;
    font-size: 8.6px; line-height: 1.75;
  }
  .letter-body p { margin-bottom: 13px; }
  .sign-off { position: absolute; left: 150px; top: 545px; font-size: 9.5px; }
  .signature-mark {
    display: block; width: 90px; height: 32px; margin: 6px 0 4px 30px;
    background: var(--signature-tone); border-radius: 3px;
  }
  .signer { margin-left: 40px; font-size: 10px; }
  .address {
    position: absolute; right: 52px; top: 640px; text-align: right; font-style: normal;
    font-size: 10.5px; line-height: 1.4; color: var(--ink-dark);
  }
  .footer-rule {
    position: absolute; left: 55px; right: 55px; top: 690px;
    height: 1.5px; background: var(--green);
  }
  .contacts {
    position: absolute; left: 85px; top: 708px;
    list-style: none; font-size: 10.5px; line-height: 1.5; color: var(--ink-dark);
  }
  .contacts li { display: flex; align-items: center; gap: 6px; }
  .contacts svg { width: 9px; height: 9px; fill: var(--green); }
</style>
</head>
<body>
<main class="letterhead">
  <header class="brand">
    <div class="brand-row">
      <span class="brand-dot"></span>
      <span class="brand-name">Halden Parcel</span>
    </div>
    <span class="brand-tagline">Clean city delivery</span>
  </header>

  <address class="recipient">
    <div class="recipient-name">Marlene Hoffer</div>
    <div class="recipient-detail">Chief Executive Officer</div>
    <div class="recipient-detail">City/State, Zip Code</div>
  </address>

  <section class="letter-body">
    <p>Thank you for choosing us for your deliveries across the city. Our electric cargo bikes and vans bring every parcel to the doorstep on time, with zero local emissions and a friendly face. We plan each route with care so that your customers enjoy a smooth experience from warehouse to front door.</p>
    <p>As one team, we share a passion for excellence. Every driver, planner and partner works toward the same goal: reliable service that respects people and the planet. We measure our performance openly and improve it every single week.</p>
    <p>We would be glad to discuss how our clean city delivery service can support your business. Please contact us at any time to arrange a meeting with our team.</p>
  </section>

  <div class="sign-off">
    <div>Sincerely,</div>
    <span class="signature-mark" role="img" aria-label="Handwritten signature"></span>
    <div class="signer">Jonas Weber</div>
  </div>

  <address class="address">
    18 Lindenweg,<br>Berlin, 10115
  </address>

  <div class="footer-rule"></div>

  <ul class="contacts">
    <li><svg viewBox="0 0 10 10"><path d="M2 0.5l2 2-1 1.2c.6 1.3 1.6 2.3 2.9 2.9l1.2-1 2 2-1.3 1.9C4.5 9.3.7 5.5.1 1.8z"/></svg>030 555 01 47</li>
    <li><svg viewBox="0 0 10 10"><path d="M0 2h10v6H0z M0 2l5 3.5L10 2" stroke="#fff" stroke-width="0.8"/></svg>hello@haldenparcel.de</li>
    <li><svg viewBox="0 0 10 10"><circle cx="5" cy="5" r="5"/></svg>www.haldenparcel.de</li>
  </ul>
</main>
</body>
</html>
```